Business card for apparel company. Specializing in fishing and boating performance wear. Main company name is Marlow Pelican Company, LLC brand name for apparel is TIDEWAKE. See website www.TidewakeBayline.com I will attach some logos to consider.

```html
<!DOCTYPE html>
<html lang="en">
<head>
<meta charset="utf-8">
<title>TIDEWAKE business card</title>
<link rel="stylesheet" href="https://fonts.googleapis.com/css2?family=Rajdhani:wght@300;400;700&family=Montserrat:ital,wght@0,300;0,400;1,300&display=swap">
<style>
  :root {
    --page: #e4e5e7;
    --card-deep: #0a3c9a;
    --card-left: #0f4fa0;
    --card-right: #0068d6;
    --band-dark: #00309e;
    --band-soft: rgba(255,255,255,0.05);
    --ink: #ffffff;
    --accent: #00a9de;
  }
  * { box-sizing: border-box; margin: 0; padding: 0; }
  html, body {
    width: 1200px; height: 1200px; overflow: hidden;
    background: var(--page);
  }
  .sheet { position: relative; width: 1200px; height: 1200px; }
  .card {
    position: absolute; left: 243px; width: 713px; height: 396px;
    border-radius: 26px; overflow: hidden;
    background: linear-gradient(90deg, var(--card-left) 0%, #0859bd 55%, var(--card-right) 100%);
    color: var(--ink);
  }
  .card--front { top: 161px; }
  .card--back { top: 640px; }
  .card__waves { position: absolute; inset: 0; width: 100%; height: 100%; }

  .brand {
    position: absolute; white-space: nowrap;
    font-family: "Rajdhani", sans-serif; font-weight: 700;
    color: var(--ink); letter-spacing: 2px; line-height: 1;
  }
  .card--front .brand { left: 50%; top: 178px; transform: translateX(-50%); font-size: 52px; }
  .card--back .brand { left: 564px; top: 236px; transform: translateX(-50%); font-size: 40px; }

  .holder { position: absolute; left: 55px; top: 58px; }
  .holder__name {
    font-family: "Rajdhani", sans-serif; font-size: 50px; line-height: 1;
    letter-spacing: 3px; white-space: nowrap;
  }
  .holder__name .first { font-weight: 300; }
  .holder__name .last { font-weight: 700; }
  .holder__role {
    position: absolute; left: 7px; top: 48px;
    font-family: "Rajdhani", sans-serif; font-weight: 400; font-size: 17px;
    letter-spacing: 1.5px; white-space: nowrap;
  }
  .holder__rule {
    position: absolute; left: 126px; top: 55px; width: 108px; height: 1.5px;
    background: linear-gradient(90deg, var(--accent) 0 50%, var(--ink) 50% 100%);
  }
  .holder__bar {
    position: absolute; left: 62px; top: 145px; width: 103px; height: 7px;
    border-radius: 2px; background: var(--accent);
  }

  .contact { position: absolute; left: 0; width: 100%; }
  .contact__icon { position: absolute; left: 68px; width: 16px; height: 16px; }
  .contact__lines {
    position: absolute; left: 110px;
    font-family: "Montserrat", sans-serif; font-weight: 300; font-size: 13.5px;
    line-height: 16px; letter-spacing: 1.6px; white-space: nowrap;
  }
  .contact--phone { top: 178px; }
  .contact--web { top: 225px; }
  .contact--place { top: 275px; }
  .contact .contact__icon { top: 8px; }

  .site {
    position: absolute; left: 64px; top: 362px;
    display: flex; align-items: center; gap: 7px;
    font-family: "Montserrat", sans-serif; font-style: italic; font-weight: 300;
    font-size: 13px; letter-spacing: 1.4px; white-space: nowrap;
  }
  .site svg { width: 12px; height: 12px; }
</style>
</head>
<body>
<div class="sheet">

  <section class="card card--front">
    <svg class="card__waves" viewBox="0 0 713 396" preserveAspectRatio="none" aria-hidden="true">
      <path d="M0 0H713V90C560 60 430 30 300 22C170 14 70 20 0 42Z" fill="var(--band-dark)" opacity="0.55"/>
      <path d="M0 42C90 18 200 14 320 28C450 44 560 80 713 140V0H0Z" fill="var(--band-soft)"/>
      <path d="M0 396V290C150 320 300 350 450 360C560 366 650 356 713 330V396Z" fill="var(--band-dark)" opacity="0.55"/>
      <path d="M0 250C180 290 330 350 480 370C580 380 660 368 713 345V396H0Z" fill="var(--band-soft)"/>
    </svg>
    <div class="brand">TIDEWAKE</div>
  </section>

  <section class="card card--back">
    <svg class="card__waves" viewBox="0 0 713 396" preserveAspectRatio="none" aria-hidden="true">
      <path d="M0 0H713V90C560 60 430 30 300 22C170 14 70 20 0 42Z" fill="var(--band-dark)" opacity="0.55"/>
      <path d="M0 42C90 18 200 14 320 28C450 44 560 80 713 140V0H0Z" fill="var(--band-soft)"/>
      <path d="M0 396V290C150 320 300 350 450 360C560 366 650 356 713 330V396Z" fill="var(--band-dark)" opacity="0.55"/>
      <path d="M0 250C180 290 330 350 480 370C580 380 660 368 713 345V396H0Z" fill="var(--band-soft)"/>
    </svg>

    <div class="holder">
      <div class="holder__name"><span class="first">YOUR </span><span class="last">NAME</span></div>
      <div class="holder__role">YOUR POSITION</div>
      <div class="holder__rule"></div>
    </div>
    <div class="holder__bar"></div>

    <div class="contact contact--phone">
      <svg class="contact__icon" viewBox="0 0 16 16" fill="none" stroke="#fff" stroke-width="1" aria-hidden="true">
        <path d="M3 1.5l2.5 2.7-1.3 1.6c.9 2 2.5 3.7 4.6 4.6l1.6-1.3 2.7 2.5-1.6 2C7 13.2 2.8 9 1.5 3.1Z"/>
      </svg>
      <div class="contact__lines">+000 2103 8894<br>+000 8899 2376</div>
    </div>

    <div class="contact contact--web">
      <svg class="contact__icon" viewBox="0 0 16 16" fill="none" stroke="#fff" stroke-width="1" aria-hidden="true">
        <circle cx="8" cy="8" r="6.5"/><ellipse cx="8" cy="8" rx="3" ry="6.5"/>
        <path d="M1.5 8h13M2.5 4.8h11M2.5 11.2h11M8 1.5v13"/>
      </svg>
      <div class="contact__lines">www.websiteurl.com<br>info@websiteurl.com</div>
    </div>

    <div class="contact contact--place">
      <svg class="contact__icon" viewBox="0 0 16 16" fill="none" stroke="#fff" stroke-width="1.1" aria-hidden="true">
        <path d="M8 12S4 8.2 4 5.2a4 4 0 0 1 8 0C12 8.2 8 12 8 12Z" fill="#fff"/>
        <circle cx="8" cy="5.2" r="1.5" fill="#0d55b0" stroke="none"/>
        <ellipse cx="8" cy="13.5" rx="5" ry="1.5"/>
      </svg>
      <div class="contact__lines">Your Address<br>Here 001234</div>
    </div>

    <div class="brand">TIDEWAKE</div>

    <div class="site">
      <svg viewBox="0 0 16 16" fill="none" stroke="#fff" stroke-width="1.1" aria-hidden="true">
        <circle cx="8" cy="8" r="6.5"/><ellipse cx="8" cy="8" rx="3" ry="6.5"/>
        <path d="M1.5 8h13M2.5 4.8h11M2.5 11.2h11M8 1.5v13"/>
      </svg>
      <span>www.TidewakeBayline.com</span>
    </div>
  </section>

</div>
</body>
</html>
```